Web Design Project

need a website, logo and a matching business Card for design studio. i have a company that works with many companies and i want to offer design services that will be outsourced to drawfolk.

this website is totally for the design services. i need it to be simple but very catcgy and trendy, yet MUST BE ELEGENT.

you being a designer will know best what do i require in this website and how it should look and feel..

i dont need many pages, most of the selling work to clients will be face to face, this is just for them to view the sample works.

the company is called "Quenbrook, Artisan Studio", so pages i need are: 1- the Studio 2- Folios 3- Contact us( will include company informaiton, and online contact form that should have a drop-down list of all types of designs.

main focus is the folios pages, it needs to have samples of works, the classification of works should be on two basis, by type of design and by designer. client should be able to select a certain designer and send an inquiry. if the customer does that, then i should get all client details and the designer should get a notification that he has been requested though no contact details of client should be given to designer as i want to make sure that those jobs are given to designer through draw folk and this is an invitation for any designer who care to put his works on the website. next to that, if the customer requires a job online then we need to get information on how design should feel and look.

please quote your price to include the website and business card design, A3 head letter and envelope.

Please provide a mock up of your design or a briefing an initial design before asking to be announced as the winner.

Target Market(s)

my customers are general managers and decision makers.

Industry/Entity Type

Business

Requirements
Must have
• ability to filiter works based on type or designer. and website must offer all types of designs included here

```html
<!DOCTYPE html>
<html lang="en">
<head>
<meta charset="utf-8">
<title>Artisan Studio</title>
<link rel="stylesheet" href="https://fonts.googleapis.com/css2?family=Arimo:wght@400;700&family=Gelasio:ital,wght@1,700&family=Jost:wght@600&display=swap">
<style>
  :root {
    --bg-deep: #5a2f1f;
    --bg-mid: #8a4c33;
    --bg-warm: #a45d3e;
    --glow: #e8b48c;
    --footer: #4f2a1c;
    --panel: rgba(235, 200, 185, 0.35);
    --field: #ffffff;
    --field-line: #c9b7ab;
    --ink: #111111;
    --muted: #555555;
    --brand: #f07a1e;
    --button-top: #f4b27a;
    --button-bottom: #d9803f;
    --contact-field: #7a5c4b;
    --contact-text: #b9a196;
    --footer-link: #ffffff;
    --footer-soft: #e9d9cf;
    --footer-mark: rgba(255, 255, 255, 0.28);
    --social: #4a2417;
  }
  * { box-sizing: border-box; margin: 0; padding: 0; }
  html, body { width: 1200px; height: 938px; overflow: hidden; }
  body {
    position: relative;
    font-family: "Arimo", Arial, sans-serif;
    background: var(--bg-mid);
    color: var(--ink);
  }
  .hero-backdrop {
    position: absolute; left: 0; top: 0; width: 1200px; height: 773px;
    background:
      radial-gradient(ellipse 260px 520px at 310px 420px, rgba(240,190,150,0.55), transparent 70%),
      radial-gradient(ellipse 700px 160px at 380px 720px, rgba(235,180,140,0.45), transparent 70%),
      linear-gradient(180deg, #9a5538 0%, var(--bg-warm) 45%, #8f4d33 100%);
  }
  .site-footer {
    position: absolute; left: 0; top: 773px; width: 1200px; height: 165px;
    background: linear-gradient(180deg, #5b3121, var(--footer));
  }
  .social { position: absolute; top: 27px; left: 921px; display: flex; gap: 13px; }
  .social span { width: 32px; height: 32px; border-radius: 50%; background: var(--social); opacity: .75; }
  .brand {
    position: absolute; left: 516px; top: 150px; display: flex; align-items: center; gap: 14px;
  }
  .brand-square { width: 60px; height: 60px; background: var(--brand); }
  .brand-name {
    font-family: "Jost", "Futura", sans-serif; font-weight: 600; font-size: 50px;
    color: var(--brand); letter-spacing: 1px;
  }
  .search-panel {
    position: absolute; left: 184px; top: 284px; width: 826px; height: 79px;
    background: var(--panel); border-radius: 8px;
    box-shadow: 0 2px 6px rgba(0,0,0,.25);
  }
  .field, .select {
    position: absolute; top: 29px; height: 23px; background: var(--field);
    border: 1px solid var(--field-line); font-size: 13px; color: var(--muted);
    padding: 4px 10px;
  }
  .select svg { position: absolute; right: 7px; top: 6px; }
  .card {
    position: absolute; top: 448px; width: 261px; height: 245px; background: #fff;
    border-radius: 6px; box-shadow: 0 2px 6px rgba(0,0,0,.35);
  }
  .card h2 {
    position: absolute; left: 17px; top: 9px;
    font-family: "Gelasio", Georgia, serif; font-style: italic; font-weight: 700; font-size: 27px;
  }
  .card p { font-size: 12px; line-height: 15px; color: var(--ink); }
  .photo { position: absolute; border-radius: 1px; }
  .btn {
    position: absolute; font-size: 11px; color: #3a1a0a; border-radius: 9px;
    background: linear-gradient(180deg, var(--button-top), var(--button-bottom));
    text-align: center; box-shadow: 0 1px 2px rgba(0,0,0,.3);
  }
  .contact-field {
    position: absolute; left: 21px; width: 217px; height: 23px; border-radius: 6px;
    background: var(--contact-field); color: var(--contact-text); font-size: 12px; padding: 5px 14px;
  }
  .footer-col { position: absolute; top: 26px; list-style: none; }
  .footer-col li { font-size: 13px; line-height: 19px; color: var(--footer-link); }
  .footer-col.soft li { color: var(--footer-soft); }
  .footer-mark {
    position: absolute; left: 777px; top: 49px; display: flex; align-items: center; gap: 8px;
  }
  .footer-mark span:first-child { width: 26px; height: 26px; background: var(--footer-mark); }
  .footer-mark span:last-child {
    font-family: "Jost", sans-serif; font-weight: 600; font-size: 25px; color: var(--footer-mark);
  }
  .legal { position: absolute; right: 196px; text-align: right; font-size: 11px; color: var(--footer-soft); }
</style>
</head>
<body>
  <div class="hero-backdrop" role="img" aria-label="Warm sepia night city skyline with a lit tower on a textured brown background"></div>

  <div class="social" aria-label="Social links"><span></span><span></span></div>

  <div class="brand">
    <span class="brand-square"></span>
    <span class="brand-name">Artisan Studio</span>
  </div>

  <form class="search-panel">
    <div class="field" style="left:32px;width:235px;">Search by</div>
    <div class="select" style="left:279px;width:111px;">Design
      <svg width="11" height="10" viewBox="0 0 11 10"><path d="M0 0h11L5.5 10z" fill="#444"/></svg></div>
    <div class="field" style="left:432px;width:236px;">Search by</div>
    <div class="select" style="left:678px;width:113px;">Designer
      <svg width="11" height="10" viewBox="0 0 11 10"><path d="M0 0h11L5.5 10z" fill="#444"/></svg></div>
  </form>

  <section class="card" style="left:185px;">
    <h2>the studio</h2>
    <div class="photo" role="img" aria-label="Bright modern studio interior with white reception desk" style="left:16px;top:48px;width:226px;height:97px;background:linear-gradient(180deg,#c9d3df,#eef1f4 45%,#8a95a6);"></div>
    <p style="position:absolute;left:17px;top:154px;width:225px;">Lorem Ipsum is simply dummy text of the printing and typesetting industry. Lorem Ipsum has been the industry's standard dummy text</p>
    <div class="btn" style="left:173px;top:214px;width:71px;height:22px;line-height:22px;">view more</div>
  </section>

  <section class="card" style="left:468px;">
    <h2>folios</h2>
    <div class="photo" role="img" aria-label="Colourful abstract swirl artwork" style="left:17px;top:51px;width:90px;height:75px;background:radial-gradient(circle at 50% 50%,#f0c04a,#e0609a 35%,#6ab0e0 65%,#cfe6f5);"></div>
    <p style="position:absolute;left:120px;top:57px;width:130px;">Lorem Ipsum is simply dummy text of the printing and typesetting industry.</p>
    <div class="photo" role="img" aria-label="Glowing neon abstract artwork on black" style="left:17px;top:141px;width:90px;height:75px;background:radial-gradient(circle at 50% 45%,#e04aa8,#5a2a6a 45%,#120a12 80%);"></div>
    <p style="position:absolute;left:120px;top:149px;width:130px;">Lorem Ipsum is simply dummy text of the printing and typesetting industry.</p>
  </section>

  <section class="card" style="left:749px;">
    <h2>quick contact</h2>
    <div class="contact-field" style="top:53px;">Name</div>
    <div class="contact-field" style="top:83px;">Email</div>
    <div class="contact-field" style="top:112px;">Phone</div>
    <div class="contact-field" style="top:143px;height:58px;">Message</div>
    <div class="btn" style="left:165px;top:213px;width:72px;height:24px;line-height:24px;font-size:12px;">Submit</div>
  </section>

  <footer class="site-footer">
    <ul class="footer-col" style="left:196px;">
      <li>Home</li><li>About us</li><li>Services</li><li>Potfolio</li><li>Projects</li><li>Contact us</li>
    </ul>
    <ul class="footer-col soft" style="left:348px;">
      <li>Terms of use</li><li>Privacy Policy</li><li>Sitemap</li><li>Careers</li>
    </ul>
    <ul class="footer-col soft" style="left:507px;">
      <li>Our Mission</li><li>Our Vision</li><li>Our Projects</li>
    </ul>
    <div class="footer-mark"><span></span><span>Artisan Studio</span></div>
    <p class="legal" style="top:119px;">© 2012 Artisan Studio</p>
    <p class="legal" style="top:136px;">Terms of Service - Privacy Policy - Program Policies</p>
  </footer>
</body>
</html>
```